Business Card Design

I need Business card designs with following on cards:

Dalton Mewse
Director

M: +61 491 268 304
D: +61 7 5590 1826
F: +61 7 5590 6071
E: dalton@torvelgroup.com.au

Torvel Group
Suite 4/58 North Calloway Road
Corvale Heads QLD 4299

Rex Halloran
Director

M: +61 438 952 107
D: +61 7 5590 1826
F: +61 7 5590 6071
E: rex@torvelgroup.com.au

Torvel Group
Corvale Heads QLD 4299

Torvel Group Logo has been attached to brief.

```html
<!DOCTYPE html>
<html lang="en">
<head>
<meta charset="utf-8">
<title>Torvel Group — Business Card</title>
<link rel="stylesheet" href="https://fonts.googleapis.com/css2?family=Saira+Condensed:wght@400;500&display=swap">
<style>
  :root {
    --page-bg: #141414;
    --green-light: #a6d83a;
    --green-mid: #3fb53a;
    --green-deep: #0f6a22;
    --ink-dark: #0b160b;
    --slate-light: #7c7f86;
    --slate-mid: #5c5f66;
    --slate-dark: #3c3e44;
    --contact-green: #37c23a;
  }
  * { margin: 0; padding: 0; box-sizing: border-box; }
  html, body {
    width: 1200px;
    height: 960px;
    overflow: hidden;
    background: var(--page-bg);
  }
  .canvas {
    position: relative;
    width: 1200px;
    height: 960px;
    font-family: "Saira Condensed", "Arial Narrow", sans-serif;
  }
  .card {
    position: absolute;
    left: 250px;
    width: 700px;
    height: 400px;
    overflow: hidden;
    box-shadow: 0 8px 24px rgba(0, 0, 0, 0.6);
  }

  /* Front */
  .card-front {
    top: 60px;
    background: radial-gradient(ellipse 60% 65% at 52% 40%, var(--green-light) 0%, var(--green-mid) 50%, var(--green-deep) 100%);
  }
  .company-name {
    position: absolute;
    left: 100px;
    top: 80px;
    font-size: 58px;
    font-weight: 500;
    letter-spacing: 2px;
    color: var(--ink-dark);
  }
  .company-address {
    position: absolute;
    left: 380px;
    top: 178px;
    font-size: 22px;
    line-height: 28px;
    font-weight: 500;
    letter-spacing: 0.5px;
    color: var(--ink-dark);
  }

  /* Back */
  .card-back {
    top: 500px;
    background: radial-gradient(ellipse 55% 60% at 48% 50%, var(--slate-light) 0%, var(--slate-mid) 55%, var(--slate-dark) 100%);
  }
  .band {
    position: absolute;
  }
  .band-top {
    left: 0;
    top: 0;
    width: 400px;
    height: 52px;
    background: radial-gradient(ellipse 60% 90% at 65% 45%, var(--green-light) 0%, var(--green-mid) 55%, var(--green-deep) 100%);
  }
  .band-side {
    left: 612px;
    top: 52px;
    width: 46px;
    height: 348px;
    background: radial-gradient(ellipse 90% 55% at 50% 60%, var(--green-light) 0%, var(--green-mid) 55%, var(--green-deep) 100%);
  }
  .person {
    position: absolute;
    left: 120px;
    top: 92px;
    width: 360px;
    text-align: center;
    font-size: 30px;
    line-height: 36px;
    color: var(--contact-green);
  }
  .contact-list {
    position: absolute;
    left: 70px;
    top: 222px;
    list-style: none;
    font-size: 22px;
    line-height: 29px;
    color: var(--contact-green);
  }
</style>
</head>
<body>
<main class="canvas">
  <section class="card card-front" aria-label="Business card front">
    <h1 class="company-name">Torvel Group</h1>
    <address class="company-address" style="font-style: normal;">
      Suite 4/58 North Calloway Road<br>
      Corvale Heads QLD 4299
    </address>
  </section>

  <section class="card card-back" aria-label="Business card back">
    <div class="band band-top"></div>
    <div class="band band-side"></div>
    <div class="person">
      <p class="person-name">Rex Halloran</p>
      <p class="person-title">Director</p>
    </div>
    <ul class="contact-list">
      <li>M: +61 438 952 107</li>
      <li>D: +61 7 5590 1826</li>
      <li>F: +61 7 5590 6071</li>
      <li>E: rex@torvelgroup.com.au</li>
    </ul>
  </section>
</main>
</body>
</html>
```